New company branded Power Point Template for presentations

We would like to have a clean and professional PowerPoint template made for our rebranding effort. It will be for our main company (Gordavexa) and will be used for both general introductory presentations and more technical industry related webinar and in-person presentations. We are a company in the manufacturing space working primarily in automotive. We provide simulation services to optimize production and softwares to allow users to do the same for themselves. The template needs to be easy to modify (even for novice users). I would like a good cover slide, content slides with common title / logo / etc. and a Q&A slide along with a final slide "Thank you" of similar. I have included our brand style guide in a high res pdf. Its images should be sufficient but please let me know if that is not the case.

```html
<!DOCTYPE html>
<html lang="en">
<head>
<meta charset="utf-8">
<title>Gordavexa – Presentation Template Overview</title>
<link href="https://fonts.googleapis.com/css2?family=Saira:wght@400;500;600&family=Montserrat:wght@400;600;700&display=swap" rel="stylesheet">
<style>
:root{
  --navy:#0c3a5e;
  --navy-deep:#082c48;
  --teal:#0f6f78;
  --cyan:#14a0b4;
  --orange:#f2a413;
  --blue:#2f6fd6;
  --grey:#a9adb1;
  --ink:#1d2a33;
  --muted:#8a9299;
  --line:#f1e4b8;
  --white:#ffffff;
}
*{margin:0;padding:0;box-sizing:border-box}
html,body{width:1200px;height:1200px;overflow:hidden;background:var(--white)}
body{position:relative;font-family:"Montserrat",sans-serif;color:var(--ink)}
.slide{position:absolute;width:260px;height:146px;overflow:hidden;background:var(--white);box-shadow:0 4px 12px rgba(0,0,0,.18)}
.abs{position:absolute}
.photo{position:absolute}
.logo{position:absolute;background:var(--navy);display:flex;flex-direction:column;align-items:center;justify-content:center;color:var(--white);box-shadow:0 2px 5px rgba(0,0,0,.25)}
.logo .mark{width:7px;height:7px;background:var(--orange);margin-bottom:3px}
.logo .name{font-family:"Saira",sans-serif;font-weight:600;font-size:4.2px;letter-spacing:.3px}
.logo .sub{font-size:2.6px;letter-spacing:.3px;margin-top:1.5px;opacity:.9}
.logo .over{position:absolute;top:4px;left:5px;font-size:2.6px}
.title{position:absolute;font-family:"Saira",sans-serif;font-weight:400;line-height:1.05;color:var(--ink)}
.tiny{position:absolute;font-size:2.7px;line-height:1.55;color:var(--muted)}
.tiny.bold{font-weight:700;color:var(--ink)}
.num{position:absolute;font-family:"Saira",sans-serif;line-height:1}
.white{color:var(--white)}
.panel{position:absolute;display:flex;align-items:center;padding-left:6px;color:var(--white)}
.panel .pn{font-family:"Saira",sans-serif;font-size:12px;margin-right:3px}
.panel .pt{font-size:2.8px;line-height:1.5}
.panel .pt b{display:block;font-size:3.2px;font-weight:600;margin-bottom:1px}
.faint{opacity:.75}
.bigletter{position:absolute;font-family:"Saira",sans-serif;font-weight:600;line-height:1}
</style>
</head>
<body>

<!-- Row 1 -->
<section class="slide cover" style="left:37px;top:149px">
  <div class="photo" role="img" aria-label="Photo of a CNC machine milling an automotive part, tinted navy and teal" style="inset:0;background:linear-gradient(120deg,#0c3a5e 0%,#14506a 45%,#1a6470 70%,#0e4a5c 100%)"></div>
  <div class="abs" style="left:0;right:0;bottom:0;height:12px;background:var(--teal)"></div>
  <div class="tiny white" style="left:0;right:0;bottom:3px;text-align:center;font-size:2.6px;letter-spacing:.6px">www.gordavexa-demo.com</div>
  <div class="logo" style="left:33px;top:33px;width:71px;height:71px"><span class="mark" style="width:10px;height:10px"></span><span class="name" style="font-size:6px">GORDAVEXA</span></div>
  <div class="title white" style="left:122px;top:53px;font-size:11px;line-height:2.1">BUSINESS<br>PRESENTATION</div>
</section>

<section class="slide toc" style="left:336px;top:149px">
  <div class="photo" role="img" aria-label="Close-up photo of copper-coloured machined parts on a milling bed" style="left:0;top:0;width:111px;height:146px;background:linear-gradient(140deg,#3b3f42,#8a5a3a 40%,#b46c3e 55%,#4a4d50)"></div>
  <div class="abs" style="left:132px;top:0;width:128px;height:42px;background:var(--cyan)"></div>
  <div class="logo" style="left:89px;top:0;width:43px;height:41px"><span class="mark"></span><span class="name">GORDAVEXA</span><span class="sub">Table Of Content</span></div>
  <div class="tiny white" style="left:160px;top:13px;font-size:4.4px;line-height:2.2">BEST OPTION TO START<br>YOUR BUSINESS.</div>
  <div class="abs" style="left:127px;top:55px;width:118px;font-size:2.7px;letter-spacing:.4px">
    <div style="display:flex;justify-content:space-between;border-bottom:.5px solid var(--line);padding-bottom:2px;margin-bottom:9px"><span>COMPANY INFO</span><span>01</span></div>
    <div style="display:flex;justify-content:space-between;border-bottom:.5px solid var(--line);padding-bottom:2px;margin-bottom:9px"><span>OUR MISSION</span><span>07</span></div>
    <div style="display:flex;justify-content:space-between;border-bottom:.5px solid var(--line);padding-bottom:2px;margin-bottom:9px"><span>WORKING PROCESS</span><span>17</span></div>
    <div style="display:flex;justify-content:space-between;border-bottom:.5px solid var(--line);padding-bottom:2px;margin-bottom:9px"><span>CASE STUDY</span><span>23</span></div>
    <div style="display:flex;justify-content:space-between;border-bottom:.5px solid var(--line);padding-bottom:2px;margin-bottom:9px"><span>SERVICES</span><span>28</span></div>
    <div style="display:flex;justify-content:space-between;border-bottom:.5px solid var(--line);padding-bottom:2px"><span>TESTIMONIALS</span><span>34</span></div>
  </div>
</section>

<section class="slide about" style="left:619px;top:149px">
  <div class="logo" style="left:14px;top:9px;width:39px;height:39px"><span class="over">About</span><span class="mark"></span><span class="name">GORDAVEXA</span></div>
  <div class="title" style="left:67px;top:15px;font-size:12.5px">Be leader of industry<br>for tomorrow.</div>
  <div class="abs" style="left:67px;top:55px;width:174px;height:.6px;background:var(--line)"></div>
  <svg class="abs" style="left:66px;top:69px" width="12" height="12" viewBox="0 0 12 12" fill="none" stroke="#2f6fd6" stroke-width=".7"><circle cx="6" cy="6" r="5"/><ellipse cx="6" cy="6" rx="2.2" ry="5"/><path d="M1 6h10M2 3.5h8M2 8.5h8"/></svg>
  <div class="tiny" style="left:67px;top:86px;font-size:3.2px;color:var(--ink)">Our Mission</div>
  <div class="tiny" style="left:67px;top:95px;width:68px"><b style="color:var(--ink)">Our tools help plants run lean and plan each line with data.</b> We model every cell, test each change first and share clear results so teams can act fast with less risk on the floor.</div>
  <div class="tiny bold" style="left:153px;top:68px;width:82px;font-weight:600;color:#3c4750">We build simulation models for automotive plants and the software teams use to run them in house. Every project starts with a clear look at flow, people and machines, then moves to tested options that cut waste and raise output. Our experts stay close through launch, sharing each result in plain words so managers and operators can trust the plan and keep improving long after we leave.</div>
</section>

<section class="slide why" style="left:910px;top:149px">
  <div class="photo" role="img" aria-label="Photo of factory ceiling and machinery in grey tones" style="left:0;top:0;width:260px;height:44px;background:linear-gradient(100deg,#6d7a82,#a9b4ba 50%,#59656d)"></div>
  <div class="photo" role="img" aria-label="Photo of a milling machine cutting a copper part" style="left:11px;top:42px;width:98px;height:92px;background:linear-gradient(150deg,#3a3e41,#9a5e3b 45%,#55595c)"></div>
  <div class="abs" style="left:0;top:42px;width:76px;height:3px;background:var(--teal)"></div>
  <div class="abs" style="left:76px;top:29px;width:172px;height:50px;background:var(--white)"></div>
  <div class="logo" style="left:76px;top:32px;width:44px;height:44px"><span class="mark"></span><span class="name">GORDAVEXA</span><span class="sub">Why Choose Us</span></div>
  <div class="title" style="left:124px;top:40px;font-size:11.5px">Create a great value<br>for tomorrow.</div>
  <div class="abs" style="left:124px;top:79px;width:124px;height:.5px;background:var(--line)"></div>
  <div class="abs" style="left:101px;top:88px;width:7px;height:7px;border-radius:50%;background:var(--teal);color:#fff;font-size:2.6px;display:flex;align-items:center;justify-content:center">01</div>
  <div class="tiny" style="left:111px;top:87px;width:60px"><b style="color:var(--ink)">Lorem ipsum</b><br>Clear plans for each line and cell shared with every team.</div>
  <div class="abs" style="left:181px;top:88px;width:7px;height:7px;border-radius:50%;background:var(--cyan);color:#fff;font-size:2.6px;display:flex;align-items:center;justify-content:center">03</div>
  <div class="tiny" style="left:191px;top:87px;width:60px"><b style="color:var(--ink)">Lorem ipsum</b><br>Proven models tested on real data before each change.</div>
  <div class="abs" style="left:101px;top:113px;width:7px;height:7px;border-radius:50%;background:var(--orange);color:#fff;font-size:2.6px;display:flex;align-items:center;justify-content:center">02</div>
  <div class="tiny" style="left:111px;top:112px;width:60px"><b style="color:var(--ink)">Lorem ipsum</b><br>Fast support from experts who know the plant floor.</div>
  <div class="abs" style="left:181px;top:113px;width:7px;height:7px;border-radius:50%;background:var(--grey);color:#fff;font-size:2.6px;display:flex;align-items:center;justify-content:center">04</div>
  <div class="tiny" style="left:191px;top:112px;width:60px"><b style="color:var(--ink)">Lorem ipsum</b><br>Software your own team can run after the first project.</div>
</section>

<!-- Row 2 -->
<section class="slide steps" style="left:37px;top:339px">
  <div class="logo" style="left:8px;top:9px;width:43px;height:43px"><span class="mark"></span><span class="name">GORDAVEXA</span><span class="sub">Working Process</span></div>
  <div class="title" style="left:61px;top:17px;font-size:12px">Our Development<br>Step By Step.</div>
  <div class="tiny bold" style="left:182px;top:19px;width:66px;font-weight:600">Each project moves from idea to launch in four clear stages with your team.</div>
  <svg class="abs" style="left:0;top:0" width="260" height="146" viewBox="0 0 260 146" fill="none">
    <g stroke="#2f8fd6" stroke-width=".6" stroke-dasharray="2 1.6">
      <circle cx="33" cy="76" r="17"/><circle cx="161" cy="76" r="17"/><circle cx="226" cy="76" r="17"/>
      <path d="M52 76h25M116 76h26M180 76h27" stroke="#0c3a5e"/>
    </g>
    <circle cx="97" cy="76" r="17" fill="#0c3a5e"/>
  </svg>
  <div class="num" style="left:26px;top:72px;font-size:7px;color:var(--blue)">01</div>
  <div class="num white" style="left:91px;top:72px;font-size:7px">02</div>
  <div class="num" style="left:154px;top:72px;font-size:7px;color:var(--blue)">03</div>
  <div class="num" style="left:219px;top:72px;font-size:7px;color:var(--blue)">04</div>
  <div class="tiny" style="left:9px;top:105px;width:48px;text-align:center"><b style="color:var(--ink);font-size:3.2px;font-weight:600">Concept</b><br><br>First look at flow, goals and the data we need.</div>
  <div class="tiny" style="left:73px;top:105px;width:48px;text-align:center"><b style="color:var(--blue);font-size:3.2px;font-weight:600">Prototype</b><br><br>A working model built and checked with your team.</div>
  <div class="tiny" style="left:137px;top:105px;width:48px;text-align:center"><b style="color:var(--ink);font-size:3.2px;font-weight:600">Beta Version</b><br><br>Options tested and tuned against live plant data.</div>
  <div class="tiny" style="left:202px;top:105px;width:48px;text-align:center"><b style="color:var(--ink);font-size:3.2px;font-weight:600">Final Launch</b><br><br>Results rolled out with training for all users.</div>
</section>

<section class="slide progress" style="left:336px;top:339px">
  <svg class="abs" style="left:0;top:0" width="140" height="146" viewBox="0 0 140 146" fill="none" stroke-width=".6">
    <path d="M70 16v116M10 73h120" stroke="#e8ecef"/>
    <g stroke="#14a0b4"><circle cx="39" cy="35" r="5"/><ellipse cx="39" cy="35" rx="2" ry="5"/><path d="M34 35h10"/></g>
    <g stroke="#a9adb1"><path d="M96 31h2l2 7h7l2-5h-10"/><circle cx="101" cy="40" r=".8"/><circle cx="106" cy="40" r=".8"/></g>
    <g stroke="#f2a413"><path d="M35 96a3.5 3.5 0 0 1 1-7 4.5 4.5 0 0 1 8.5 1.5 3 3 0 0 1 0 5.5M39 98v-6l-2 2m2-2 2 2"/></g>
    <g stroke="#0c3a5e"><rect x="96" y="89" width="10" height="7"/><path d="M96 89l5 4 5-4"/></g>
  </svg>
  <div class="num" style="left:14px;top:48px;width:50px;text-align:center;font-size:6.5px;color:var(--cyan)">1,547m</div>
  <div class="tiny bold" style="left:14px;top:56px;width:50px;text-align:center;font-size:2.8px">Units modelled<br>in one year</div>
  <div class="num" style="left:76px;top:48px;width:50px;text-align:center;font-size:6.5px;color:var(--grey)">1,14k</div>
  <div class="tiny bold" style="left:76px;top:56px;width:50px;text-align:center;font-size:2.8px">Lines planned<br>for clients</div>
  <div class="num" style="left:14px;top:106px;width:50px;text-align:center;font-size:6.5px;color:var(--orange)">300k</div>
  <div class="tiny bold" style="left:14px;top:114px;width:50px;text-align:center;font-size:2.8px">Hours saved<br>on the floor</div>
  <div class="num" style="left:76px;top:106px;width:50px;text-align:center;font-size:6.5px;color:var(--navy)">17,014</div>
  <div class="tiny bold" style="left:76px;top:114px;width:50px;text-align:center;font-size:2.8px">Users on our<br>software today</div>
  <div class="logo" style="left:147px;top:16px;width:43px;height:43px"><span class="mark"></span><span class="name">GORDAVEXA</span><span class="sub">Working Process</span></div>
  <div class="title" style="left:198px;top:20px;font-size:10.5px">Our<br>Progress<br>Through</div>
  <div class="tiny bold" style="left:147px;top:66px;width:100px;font-weight:600">Our numbers grow with every plant we support. Each model we build adds data that makes the next one faster and more exact. Teams see waste drop, output rise and plans that hold up once the line goes live. We track each result and share it with clients so the gains stay visible long after launch and every new project starts from a stronger base of proven work.</div>
</section>

<section class="slide influence" style="left:619px;top:339px">
  <div class="photo" role="img" aria-label="Photo of machined metal parts, tinted teal to olive and orange" style="inset:0;background:linear-gradient(100deg,#0f5a68 0%,#336e62 40%,#8a8a3c 75%,#c49a2a 100%)"></div>
  <div class="abs" style="left:0;top:92px;width:260px;height:54px;background:var(--white)"></div>
  <div class="logo" style="left:30px;top:15px;width:39px;height:41px"><span class="mark"></span><span class="name">GORDAVEXA</span></div>
  <div class="abs" style="left:78px;top:39px;width:7px;height:7px;border-radius:50%;background:var(--cyan);color:#fff;font-size:3.5px;display:flex;align-items:center;justify-content:center">x</div>
  <div class="title white" style="left:80px;top:20px;font-size:12px">Growing Influence</div>
  <div class="tiny white faint" style="left:98px;top:38px;width:150px">Our models now guide lines in many plants, helping teams plan with care and grow output with less waste.</div>
  <div class="abs" style="left:14px;top:67px;width:66px;height:64px;background:var(--teal);padding:5px 6px;color:#fff">
    <div style="font-size:2.8px;font-weight:600">YOUR TITLE HERE</div>
    <div style="font-size:2.6px;line-height:1.55;opacity:.7;margin-top:2px">Faster cycle time on each line after a model based plan was put in place.</div>
    <div style="font-family:Saira,sans-serif;font-size:8px;position:absolute;left:19px;bottom:6px">74.11%</div>
  </div>
  <div class="abs" style="left:94px;top:67px;width:66px;height:64px;background:var(--cyan);padding:5px 6px;color:#fff">
    <div style="font-size:2.8px;font-weight:600">YOUR TITLE HERE</div>
    <div style="font-size:2.6px;line-height:1.55;opacity:.75;margin-top:2px">Share of clients who keep using our software after the first project.</div>
    <div style="font-family:Saira,sans-serif;font-size:8px;position:absolute;left:18px;bottom:6px">87.34%</div>
  </div>
  <div class="abs" style="left:193px;top:76px;width:34px;height:34px;border-radius:50%;background:var(--navy)"></div>
  <div class="tiny" style="left:178px;top:115px;width:64px;text-align:center;font-size:2.6px;letter-spacing:.2px">STEADY GROWTH IN<br>CLIENT PLANTS AND<br>SOFTWARE USERS</div>
</section>

<section class="slide options" style="left:910px;top:339px">
  <div class="photo" role="img" aria-label="Photo of industrial milling equipment in grey steel tones" style="left:0;top:0;width:100px;height:146px;background:linear-gradient(160deg,#4f575c,#7c858a 50%,#3f464a)"></div>
  <div class="panel" style="left:14px;top:12px;width:112px;height:37px;background:var(--navy)"><span class="pn">01.</span><span class="pt"><b>Development</b>Plan each line with tested<br>models before you build</span></div>
  <div class="panel" style="left:14px;top:53px;width:112px;height:39px;background:var(--teal)"><span class="pn">02.</span><span class="pt"><b>Web Design</b>Clear dashboards that let<br>every team see results</span></div>
  <div class="panel" style="left:14px;top:96px;width:112px;height:37px;background:var(--cyan)"><span class="pn">03.</span><span class="pt"><b>Marketing</b>Share proven gains with<br>partners and buyers</span></div>
  <div class="abs" style="left:188px;top:16px;display:flex;align-items:center;font-family:Saira,sans-serif;font-weight:600;font-size:4.4px;color:var(--navy)"><span style="width:6px;height:6px;background:var(--cyan);margin-right:2px"></span>GORDAVEXA</div>
  <div class="title" style="left:148px;top:32px;font-size:12px">Options Slide</div>
  <div class="tiny" style="left:148px;top:48px;width:100px;color:#3c4750">Pick the service that fits your plant. Each one can run alone or as part of a full program led by our team.</div>
  <div class="abs" style="left:148px;top:75px;width:105px;font-size:5.4px;line-height:2.25;color:var(--ink)">Proactively disseminate cross-<br>platform <span style="color:var(--blue)">human capital</span><br>objectively functionalities.<br>orchestrate turnkey metrics<br>rather</div>
</section>

<!-- Row 3 -->
<section class="slide awesome" style="left:37px;top:531px">
  <div class="photo" role="img" aria-label="Photo of a milling machine, tinted teal to olive" style="inset:0;background:linear-gradient(100deg,#0f5a68 0%,#2e6a5e 45%,#7a7a40 80%,#a68a36 100%)"></div>
  <div class="logo" style="left:15px;top:6px;width:41px;height:38px"><span class="mark"></span><span class="name">GORDAVEXA</span></div>
  <div class="title white" style="left:61px;top:12px;font-size:11.5px">Awesome<br>Services</div>
  <div class="tiny white faint" style="left:126px;top:18px;width:120px">Services that help each plant plan better lines, cut waste and raise output with clear data.</div>
  <div class="panel" style="left:14px;top:53px;width:114px;height:38px;background:var(--navy)"><span class="pn">01.</span><span class="pt"><b>Development</b>Plan each line with tested<br>models before you build</span></div>
  <div class="panel" style="left:131px;top:53px;width:116px;height:38px;background:var(--teal)"><span class="pn">03.</span><span class="pt"><b>Marketing</b>Share proven gains with<br>partners and buyers</span></div>
  <div class="panel" style="left:14px;top:94px;width:114px;height:38px;background:var(--cyan)"><span class="pn">02.</span><span class="pt"><b>Web Design</b>Clear dashboards that let<br>every team see results</span></div>
  <div class="panel" style="left:131px;top:94px;width:116px;height:38px;background:var(--grey)"><span class="pn">04.</span><span class="pt"><b>Seo Analysis</b>Find and fix the slow<br>steps in every process</span></div>
</section>

<section class="slide services-dark" style="left:336px;top:531px">
  <div class="photo" role="img" aria-label="Photo of a CNC machine cutting a copper part" style="left:0;top:0;width:183px;height:125px;background:linear-gradient(140deg,#3b3f42,#8c5638 40%,#b86d3f 55%,#3d4245)"></div>
  <div class="abs" style="left:137px;top:17px;width:123px;height:129px;background:var(--navy)"></div>
  <div class="abs" style="left:148px;top:26px;display:flex;align-items:center;font-family:Saira,sans-serif;font-weight:600;font-size:4.4px;color:#fff"><span style="width:6px;height:6px;background:var(--cyan);margin-right:2px"></span>GORDAVEXA</div>
  <div class="title white" style="left:148px;top:40px;font-size:10px">Our Great Services.</div>
  <svg class="abs" style="left:0;top:0" width="260" height="146" viewBox="0 0 260 146" fill="none" stroke="#f2a413" stroke-width=".6">
    <circle cx="157" cy="71" r="6"/><circle cx="157" cy="97" r="6"/><circle cx="157" cy="124" r="6"/>
    <g fill="#fff" stroke="none"><circle cx="157" cy="71" r=".6"/><circle cx="156" cy="97" r=".6"/><circle cx="158" cy="97" r=".6"/><circle cx="155" cy="124" r=".6"/><circle cx="157" cy="124" r=".6"/><circle cx="159" cy="124" r=".6"/></g>
  </svg>
  <div class="tiny white" style="left:173px;top:65px;width:80px"><b style="font-size:3.2px;font-weight:600">Conception</b><br><span style="opacity:.7">Plan each new line with a tested model first</span></div>
  <div class="tiny white" style="left:173px;top:91px;width:80px"><b style="font-size:3.2px;font-weight:600">Prototype</b><br><span style="opacity:.7">Check every option with real plant data</span></div>
  <div class="tiny white" style="left:173px;top:118px;width:80px"><b style="font-size:3.2px;font-weight:600">Marketing</b><br><span style="opacity:.7">Share proven gains with all partners</span></div>
</section>

<section class="slide testimonial" style="left:619px;top:531px">
  <div class="abs" style="left:0;top:12px;width:260px;height:61px;background:linear-gradient(90deg,#0c3a5e,#0f6f78 60%,#14899a)"></div>
  <div class="abs" style="left:0;top:12px;width:150px;height:1.6px;background:var(--orange)"></div>
  <div class="photo" role="img" aria-label="Round photo of a machined metal part" style="left:13px;top:47px;width:52px;height:52px;border-radius:50%;background:linear-gradient(140deg,#4a4e51,#9a5e3b 50%,#55595c);border:1.2px solid #fff"></div>
  <div class="logo" style="left:97px;top:22px;width:43px;height:42px"><span class="mark"></span><span class="name">GORDAVEXA</span><span class="sub">Testimonials</span></div>
  <div class="title white" style="left:157px;top:21px;font-size:11px">What our<br>clients<br>has to say</div>
  <div class="tiny" style="left:9px;top:107px;width:60px;text-align:center;font-size:3.2px;color:var(--blue)">Marten Oakley</div>
  <div class="tiny" style="left:9px;top:113px;width:60px;text-align:center;font-size:2.4px;letter-spacing:.3px">DIRECTOR</div>
  <div class="tiny" style="left:115px;top:91px;width:120px">The model showed us where our body shop lost time. We fixed two stations and gained a full shift of output each week. The team was clear, quick and easy to work with from start to end.</div>
  <div class="tiny" style="left:115px;top:121px;font-size:4px;letter-spacing:.6px;color:var(--orange)">★★★★★</div>
</section>

<section class="slide break" style="left:910px;top:531px">
  <div class="photo" role="img" aria-label="Photo of machined parts, tinted teal to orange" style="inset:0;background:linear-gradient(100deg,#0f5a68 0%,#2f6b5f 40%,#8f843a 75%,#d59a1c 100%)"></div>
  <div class="logo" style="left:56px;top:43px;width:55px;height:76px"><span class="mark" style="width:10px;height:10px"></span><span class="name" style="font-size:5px">GORDAVEXA</span></div>
  <div class="title white" style="left:122px;top:35px;font-size:27px;font-weight:500;line-height:1.12;letter-spacing:.5px">Break<br>slide</div>
</section>

<!-- Row 4 -->
<section class="slide swot-s" style="left:37px;top:721px">
  <div class="photo" role="img" aria-label="Faded photo of factory machinery in teal and grey" style="left:90px;top:0;width:170px;height:146px;background:linear-gradient(90deg,rgba(255,255,255,1),rgba(150,170,175,.6) 50%,#6b8a90)"></div>
  <div class="bigletter" style="left:150px;top:-6px;font-size:170px;color:rgba(255,255,255,.45)">S</div>
  <div class="logo" style="left:14px;top:6px;width:43px;height:43px"><span class="mark"></span><span class="name">GORDAVEXA</span><span class="sub">Swot Analysis</span></div>
  <div class="title" style="left:61px;top:21px;font-size:12px">Strengths</div>
  <div class="num" style="left:15px;top:55px;font-size:11px;color:var(--navy)">01.</div>
  <div class="tiny" style="left:15px;top:68px;width:50px"><b style="color:var(--ink)">Title Goes Here</b><br>Deep know-how of the<br>automotive plant floor</div>
  <div class="num" style="left:72px;top:55px;font-size:11px;color:var(--cyan)">02.</div>
  <div class="tiny" style="left:72px;top:68px;width:50px"><b style="color:var(--ink)">Title Goes Here</b><br>Software clients can<br>run on their own</div>
  <div class="num" style="left:15px;top:98px;font-size:11px;color:var(--navy)">03.</div>
  <div class="tiny" style="left:15px;top:112px;width:50px"><b style="color:var(--ink)">Title Goes Here</b><br>Proven results in many<br>plants and regions</div>
  <div class="num" style="left:72px;top:98px;font-size:11px;color:var(--grey)">04.</div>
  <div class="tiny" style="left:72px;top:112px;width:50px"><b style="color:var(--ink)">Title Goes Here</b><br>Fast and close support<br>from our experts</div>
</section>

<section class="slide swot-w" style="left:336px;top:721px">
  <div class="photo" role="img" aria-label="Faded photo of machinery in teal tones" style="left:0;top:0;width:200px;height:146px;background:linear-gradient(90deg,#0f6f78,#3f9aa2 45%,rgba(255,255,255,0))"></div>
  <div class="bigletter" style="left:2px;top:5px;font-size:150px;color:rgba(255,255,255,.35)">W</div>
  <div class="logo" style="left:127px;top:9px;width:43px;height:42px"><span class="mark"></span><span class="name">GORDAVEXA</span><span class="sub">Swot Analysis</span></div>
  <div class="title" style="left:172px;top:26px;font-size:12px">Weaknesses</div>
  <div class="abs" style="left:172px;top:58px;width:80px;height:.5px;background:var(--line)"></div>
  <div class="num" style="left:140px;top:69px;font-size:11px;color:var(--cyan)">01.</div>
  <div class="tiny" style="left:159px;top:67px;width:90px"><b style="color:var(--ink)">Competitors</b><br>Larger firms offer wider<br>software suites today</div>
  <div class="num" style="left:140px;top:98px;font-size:11px;color:var(--cyan)">02.</div>
  <div class="tiny" style="left:159px;top:96px;width:90px"><b style="color:var(--ink)">Foreign Policy</b><br>Trade rules slow some<br>projects in new markets</div>
  <div class="tiny" style="left:144px;top:124px;width:110px;opacity:.6">Each gap has a plan and an owner to close it in the next year.</div>
</section>

<section class="slide swot-o" style="left:619px;top:721px">
  <div class="photo" role="img" aria-label="Faded photo of machined parts in warm orange tones" style="left:80px;top:0;width:180px;height:146px;background:linear-gradient(90deg,rgba(255,255,255,0),rgba(246,205,140,.7) 50%,#f2b24a)"></div>
  <div class="bigletter" style="left:130px;top:-8px;font-size:160px;color:rgba(255,255,255,.4)">O</div>
  <div class="logo" style="left:15px;top:2px;width:43px;height:43px"><span class="mark"></span><span class="name">GORDAVEXA</span><span class="sub">Swot Analysis</span></div>
  <div class="title" style="left:66px;top:19px;font-size:12px">Opportunities</div>
  <div class="tiny bold" style="left:15px;top:55px;width:110px;font-weight:600">Electric vehicle plants need new line plans and fresh models for every battery and body shop.</div>
  <div class="tiny" style="left:15px;top:79px;width:112px">Growing demand for in-house simulation opens room for our software, training and long term support deals with both new and current clients.</div>
  <div class="num" style="left:15px;top:116px;font-size:6px;color:var(--blue)">1,57m</div>
  <div class="tiny bold" style="left:15px;top:124px;font-size:2.6px">Clients Global</div>
  <div class="num" style="left:60px;top:116px;font-size:6px;color:var(--blue)">1,14k</div>
  <div class="tiny bold" style="left:60px;top:124px;font-size:2.6px">Annual Grows</div>
  <div class="num" style="left:104px;top:116px;font-size:6px;color:var(--blue)">+174</div>
  <div class="tiny bold" style="left:104px;top:124px;font-size:2.6px">New Buyers</div>
</section>

<section class="slide swot-t" style="left:910px;top:721px">
  <div class="photo" role="img" aria-label="Faded photo of machinery in grey tones" style="left:0;top:0;width:190px;height:146px;background:linear-gradient(90deg,#8e9294,#b8bbbd 50%,rgba(255,255,255,0))"></div>
  <div class="bigletter" style="left:5px;top:-8px;font-size:160px;color:rgba(255,255,255,.45)">T</div>
  <div class="logo" style="left:137px;top:4px;width:44px;height:42px"><span class="mark"></span><span class="name">GORDAVEXA</span><span class="sub">Swot Analysis</span></div>
  <div class="title" style="left:186px;top:20px;font-size:12px">Threats</div>
  <div class="abs" style="left:144px;top:52px;width:105px;height:.5px;background:var(--line)"></div>
  <div class="tiny bold" style="left:144px;top:57px;width:105px;font-weight:600;font-size:2.7px">NEW RIVALS AND CHANGING RULES MAY<br>SLOW GROWTH IN KEY MARKETS</div>
  <div class="tiny" style="left:144px;top:67px;width:105px;opacity:.6">Price pressure from low cost tools and tighter budgets at car makers could delay new projects, so we keep value clear in every offer.</div>
  <div class="num" style="left:144px;top:107px;font-size:7px;color:var(--blue)">1.7m</div>
  <div class="tiny" style="left:144px;top:115px;width:45px">Budget at risk across<br>open deals this year</div>
  <div class="num" style="left:203px;top:107px;font-size:7px;color:var(--blue)">17+</div>
  <div class="tiny" style="left:203px;top:115px;width:45px">New rivals seen in<br>the last two years</div>
</section>

<!-- Row 5 -->
<section class="slide services-grid" style="left:37px;top:912px">
  <div class="logo" style="left:15px;top:10px;width:43px;height:43px"><span class="mark"></span><span class="name">GORDAVEXA</span><span class="sub">Services.</span></div>
  <div class="title" style="left:66px;top:15px;font-size:11.5px">Our Great<br>Services.</div>
  <div class="tiny bold" style="left:140px;top:22px;width:108px;font-weight:600">A full set of tools and services to plan, test and improve every line in your automotive plant.</div>
  <div class="abs" style="left:15px;top:56px;width:232px;height:.5px;background:var(--line)"></div>
  <svg class="abs" style="left:0;top:0" width="260" height="146" viewBox="0 0 260 146" fill="none" stroke-width=".6">
    <g stroke="#0c3a5e"><rect x="15" y="62" width="10" height="7"/><path d="M18 71h4"/></g>
    <g stroke="#0c3a5e"><rect x="96" y="64" width="12" height="6"/><path d="M102 64v-3"/></g>
    <g stroke="#f2a413"><rect x="177" y="63" width="11" height="8" rx="1"/><circle cx="182.5" cy="67" r="2"/></g>
    <g stroke="#a9adb1"><path d="M15 101h8v9h-8z M17 99h8v9"/></g>
    <g stroke="#0c3a5e"><rect x="96" y="100" width="11" height="8"/><path d="M96 100l5.5 4 5.5-4"/></g>
  </svg>
  <div class="tiny" style="left:15px;top:73px;width:70px"><b style="color:var(--ink)">Lorem Ipsum</b><br>Line design and layout studies for each new plant build.</div>
  <div class="tiny" style="left:96px;top:73px;width:70px"><b style="color:var(--ink)">Lorem Ipsum</b><br>Cycle time models that show every slow step clearly.</div>
  <div class="tiny" style="left:177px;top:73px;width:70px"><b style="color:var(--ink)">Lorem Ipsum</b><br>Plant data capture and review with your own team.</div>
  <div class="tiny" style="left:15px;top:110px;width:70px"><b style="color:var(--ink)">Lorem Ipsum</b><br>Software licences with training for every new user.</div>
  <div class="tiny" style="left:96px;top:110px;width:70px"><b style="color:var(--ink)">Lorem Ipsum</b><br>Support on call for teams running their own models.</div>
  <div class="abs" style="left:177px;top:97px;width:70px;height:37px;background:var(--navy)"></div>
  <div class="tiny white" style="left:195px;top:103px;font-size:3.2px">INSPIRING<br>FOR SUCCESS</div>
  <svg class="abs" style="left:183px;top:118px" width="14" height="14" viewBox="0 0 14 14" fill="none" stroke="#fff" stroke-width=".6"><circle cx="7" cy="7" r="6"/><ellipse cx="7" cy="7" rx="2.6" ry="6"/><path d="M1 7h12M2 4h10M2 10h10"/></svg>
</section>

<section class="slide pricing" style="left:336px;top:912px">
  <div class="logo" style="left:21px;top:8px;width:35px;height:36px"><span class="mark"></span><span class="name">GORDAVEXA</span></div>
  <div class="title" style="left:64px;top:11px;font-size:12px">Pricing Table</div>
  <div class="tiny" style="left:64px;top:27px;width:185px;color:#3c4750">Choose the plan that fits your plant. Every tier includes model setup, user training and support from our team, with clear pricing and no hidden fees for updates or extra seats.</div>
  <svg class="abs" style="left:0;top:0" width="260" height="146" viewBox="0 0 260 146">
    <rect x="40" y="52" width="192" height="15" fill="#0f6f78"/>
    <rect x="26" y="67" width="13" height="53" fill="#8d9296"/>
    <g fill="#f4f5f6"><rect x="40" y="67" width="192" height="13"/><rect x="40" y="93" width="192" height="13"/></g>
    <g stroke="#e3e6e8" stroke-width=".4"><path d="M40 80h192M40 93h192M40 106h192M40 120h192M121 52v68M158 52v68M195 52v68"/></g>
    <rect x="121" y="120" width="111" height="13" fill="#cfd2d4"/>
    <g font-family="Montserrat, sans-serif" font-size="2.7" fill="#fff">
      <text x="49" y="61">NAME TITLE GOES HERE</text><text x="130" y="61">COLUMN #1</text><text x="167" y="61">COLUMN #2</text><text x="204" y="61">COLUMN #3</text>
      <text x="30" y="75">01</text><text x="30" y="88">02</text><text x="30" y="101">03</text><text x="30" y="114">04</text>
    </g>
    <g font-family="Montserrat, sans-serif" font-size="2.6" fill="#3c4750">
      <text x="49" y="75">First Feature Title Goes Here</text><text x="49" y="88">Second Feature Title</text><text x="49" y="101">Third Feature Title Goes Here</text><text x="49" y="114">Fourth Feature Title Goes Here</text>
    </g>
    <g font-family="Montserrat, sans-serif" font-size="2.6" fill="#b0b5b9" text-anchor="middle">
      <text x="139" y="75">Unlimited</text><text x="176" y="75">200 GB</text><text x="213" y="75">20 GB</text>
      <text x="139" y="88">Available</text><text x="176" y="88">400 GB</text><text x="213" y="88">40 GB</text>
      <text x="139" y="101">3 Domain</text><text x="176" y="101">2 TB</text><text x="213" y="101">100 GB</text>
      <text x="139" y="114">4 Domain</text><text x="176" y="114">500 GB</text><text x="213" y="114">50 GB</text>
    </g>
    <g font-family="Montserrat, sans-serif" font-size="2.8" fill="#fff" text-anchor="middle">
      <text x="139" y="128">Free</text><text x="176" y="128">$ 490</text><text x="213" y="128">$ 790</text>
    </g>
  </svg>
</section>

<section class="slide chart" style="left:619px;top:912px">
  <div class="logo" style="left:21px;top:8px;width:36px;height:36px"><span class="mark"></span><span class="name">GORDAVEXA</span></div>
  <div class="title" style="left:64px;top:11px;font-size:12px">Chart Slide</div>
  <div class="tiny" style="left:64px;top:27px;width:185px;color:#3c4750">Track output across the year and spot the months where each line gains or loses time, so your team can plan the next change with clear data in hand.</div>
  <svg class="abs" style="left:0;top:0" width="260" height="146" viewBox="0 0 260 146" fill="none">
    <g stroke="#eef0f2" stroke-width=".4"><path d="M14 62h136M14 72h136M14 82h136M14 92h136M14 102h136M14 112h136M14 122h136M14 132h136"/></g>
    <path d="M20 120 C26 100,30 70,36 72 S44 128,52 125 S64 72,72 68 S84 112,92 105 S100 80,106 84 S114 108,120 100 S130 80,136 82 S144 104,148 100" stroke="#f2a413" stroke-width=".9"/>
    <circle cx="72" cy="68" r="1.3" fill="#f2a413"/>
    <rect x="69" y="51" width="43" height="13" fill="#f2a413"/>
    <path d="M70 64l2 3 2-3z" fill="#f2a413"/>
    <text x="90.5" y="59.5" font-family="Montserrat, sans-serif" font-size="3.4" fill="#fff" text-anchor="middle">$ 417,198</text>
    <g font-family="Montserrat, sans-serif" font-size="2" fill="#b0b5b9">
      <text x="18" y="138">Jan</text><text x="29" y="138">Feb</text><text x="40" y="138">Mar</text><text x="51" y="138">Apr</text><text x="62" y="138">May</text><text x="73" y="138">Jun</text><text x="84" y="138">Jul</text><text x="95" y="138">Aug</text><text x="106" y="138">Sep</text><text x="117" y="138">Oct</text><text x="128" y="138">Nov</text><text x="139" y="138">Dec</text>
    </g>
  </svg>
  <div class="num" style="left:171px;top:70px;font-size:12px;color:var(--blue)">01.</div>
  <div class="tiny" style="left:191px;top:68px;width:58px"><b style="color:var(--ink);font-size:3px;font-weight:600">Annual Report</b><br>Full year output and gains for each line</div>
  <div class="num" style="left:171px;top:106px;font-size:12px;color:var(--blue)">02.</div>
  <div class="tiny" style="left:191px;top:104px;width:58px"><b style="color:var(--ink);font-size:3px;font-weight:600">Monthly Grows</b><br>Month by month change in cycle time</div>
</section>

<section class="slide thanks" style="left:910px;top:912px">
  <div class="photo" role="img" aria-label="Photo of machinery, tinted navy to olive and orange" style="inset:0;background:linear-gradient(100deg,#0c3a5e 0%,#1c5060 35%,#5c6a40 65%,#c08a22 100%)"></div>
  <div class="abs" style="left:0;right:0;top:65px;text-align:center;padding-left:10px;font-family:Saira,sans-serif;font-weight:600;font-size:7px;letter-spacing:.8px;color:#fff">GORDAVEXA</div>
  <div class="title white" style="left:0;right:0;top:74px;text-align:center;padding-left:10px;font-size:28px;font-weight:500">Thank you!</div>
</section>

</body>
</html>
```